Varubo - Nutritious Snacks and Desserts

We need a creative e-commerce website in which all features--buttons, background, etc.--convey our message: We sell delicious, nutritious snacks and desserts that most closely comply with the paleo diet guidelines. Our first product is Grenamo®--raw, vegan, paleo chocolate balls that are made of dates, coconut, and cocoa. Our products are organic, raw, irresistible and nutritious. We have several versions of Grenamo® in development, as well as mousse, ice cream, and crackers. Our mission is to purvey basic healthy foods. Our motto is, "Fuel for the Daily Trail-Seeker(tm)."

Target Market(s)

Health-conscious professionals who tend to shop at health food stores. Our products also meet the requirements of a gluten-free diet; and they also don't contain refined sugar, so shoppers with gluten and possibly sugar issues are incidental customers.

Industry/Entity Type

Health Product

Coding

Coded - Design and coding required

Number of Pages Required

5+ page

Colors

Designer to choose colors to be used in the design.

Requirements
Must have
• We need at least a home page, a products page, an about-us page, a contact page, and a shopping cart page. We would like to be able to add products on our own later. We should be able to handle some basic coding, especially if it's just a matter of copying and modifying product pages. We would also like the ability in the future to add blogging pages, allowing us to write articles about health food and healthy lifestyle, thus attracting web-traffic (SEO).
• Other features we would like to have:
• Product photo slider on the hopepage
• Back-to-top button at the bottom of the home page
• Make sure the site is mobile-compatible
• A search bar at the top of the homepage
• "Create an account" and "Previous orders"--allowing customers to see their previous orders and reorder what they purchased in the past.
Nice to have
• We would like to convey the paleo theme without actually stating it anywhere. We'll add text as necessary, according to the page layout; you can use ipsum lorem for purpose of demonstration.

```html
<!DOCTYPE html>
<html lang="en">
<head>
<meta charset="utf-8">
<title>Varubo Foods – Nutritious Snacks and Desserts</title>
<link rel="stylesheet" href="https://fonts.googleapis.com/css2?family=Lato:wght@300;400;700;900&family=Dosis:wght@500;600&family=Satisfy&display=swap">
<style>
:root{
  --coral:#ef6a5d;
  --coral-btn:#f0564e;
  --green:#7cc242;
  --ink:#1d1d1d;
  --olive-ink:#2f3a10;
  --muted:#6b6b6b;
  --white:#ffffff;
  --dark-band:#242424;
  --grey-band:#efefef;
  --sky:#bfe7ee;
  --teal:#4dc3a6;
  --navy:#2a3470;
  --soft-pink:#fcedf1;
}
*{margin:0;padding:0;box-sizing:border-box}
html,body{width:1200px;height:3600px;overflow:hidden;background:var(--white)}
body{position:relative;font-family:'Lato',sans-serif;color:var(--ink)}
.abs{position:absolute}

/* top bar */
.top-bar{left:0;top:0;width:1200px;height:36px;background:var(--coral);color:var(--white);font-size:12px;font-weight:700;letter-spacing:.3px}
.top-bar .promo{left:214px;top:11px}
.top-bar .contact{right:214px;top:11px}

/* header */
.site-header{left:0;top:36px;width:1200px;height:156px;background:var(--white)}
.brand{left:262px;top:50px;display:flex;align-items:center;gap:12px}
.brand-dot{width:36px;height:36px;border-radius:50%;background:var(--green)}
.brand-name{font-size:38px;font-weight:700;color:var(--green);letter-spacing:1px;line-height:1}
.account-links{right:216px;top:45px;font-size:12px;font-weight:700;word-spacing:4px}
.main-nav{right:216px;top:94px;display:flex;align-items:center;gap:16px;font-size:12.5px;font-weight:900}
.main-nav svg{display:block}

/* hero */
.hero{left:0;top:192px;width:1200px;height:557px;
  background:
    radial-gradient(ellipse 260px 200px at 1010px 120px,rgba(210,190,150,.35),transparent 70%),
    radial-gradient(ellipse 220px 260px at 560px 110px,rgba(170,140,110,.35),transparent 70%),
    radial-gradient(ellipse 240px 300px at 190px 330px,rgba(120,110,100,.45),transparent 70%),
    radial-gradient(ellipse 300px 160px at 850px 470px,rgba(150,130,100,.35),transparent 70%),
    radial-gradient(ellipse 180px 220px at 760px 250px,rgba(90,100,70,.35),transparent 70%),
    linear-gradient(135deg,#3a3631 0%,#4d4740 40%,#3b3a33 70%,#2d2c28 100%)}
.hero-title{left:0;top:188px;width:1200px;text-align:center;color:var(--green);font-size:44px;font-weight:700;letter-spacing:-.5px}
.hero-tagline{left:0;top:268px;width:1200px;text-align:center;color:var(--green);font-size:24px;font-weight:700}

/* intro */
.intro{left:0;top:784px;width:1200px;text-align:center;color:var(--olive-ink);font-weight:700}
.intro .lead{font-size:20px;margin-bottom:2px}
.intro p{font-size:16.5px;line-height:24px}

/* section headings */
.section-title{left:0;width:1200px;text-align:center;font-weight:700;font-size:30px;color:var(--ink)}
.section-rule{left:576px;width:48px;height:3px;background:var(--ink)}

/* products */
.product-label{font-size:15px;text-align:center;color:var(--ink)}
.media-grenamo{left:288px;top:1056px;width:384px;height:384px;
  background:
    radial-gradient(circle at 50% 62%,#6b4a2e 0 42px,transparent 44px),
    radial-gradient(circle at 50% 50%,#b08654 0,#a57a49 150px,#8a6238 172px,#f4f1ec 175px,#f7f5f1 100%)}
.media-cups{left:746px;top:1051px;width:238px;height:175px;
  background:
    radial-gradient(ellipse 55px 22px at 50% 22%,#7ad8c2,transparent 100%),
    linear-gradient(180deg,transparent 15%,transparent 15%),
    radial-gradient(ellipse 60px 80px at 50% 55%,#54c2a8 0,#72d0bb 60%,transparent 100%),
    var(--soft-pink)}
.media-jimmies{left:746px;top:1279px;width:238px;height:180px;
  background:
    radial-gradient(circle at 50% 50%,#f28fb0 0,#f5b4c9 40px,#ffffff 46px,#f3f3f3 58px,transparent 62px),
    var(--soft-pink)}
.media-toppers{left:214px;top:1505px;width:237px;height:175px;
  background:
    radial-gradient(circle at 30% 30%,#f6a7b8 0 9px,transparent 10px),
    radial-gradient(circle at 52% 26%,#f6a7b8 0 9px,transparent 10px),
    radial-gradient(circle at 72% 34%,#f6a7b8 0 9px,transparent 10px),
    radial-gradient(circle at 38% 56%,#f6a7b8 0 9px,transparent 10px),
    radial-gradient(circle at 62% 60%,#f6a7b8 0 9px,transparent 10px),
    radial-gradient(circle at 46% 80%,#f6a7b8 0 9px,transparent 10px),
    var(--soft-pink)}
.media-nonpareils{left:214px;top:1733px;width:237px;height:168px;
  background:
    radial-gradient(circle at 50% 50%,#a6dc8a 0,#b8e49f 44px,#ffffff 50px,#eeeeee 58px,transparent 62px),
    var(--soft-pink)}
.media-mousse{left:480px;top:1541px;width:504px;height:336px;
  background:
    radial-gradient(ellipse 40px 26px at 300px 70px,#d8343c,transparent 100%),
    radial-gradient(ellipse 22px 18px at 50px 240px,#cf2f36,transparent 100%),
    radial-gradient(ellipse 100px 140px at 300px 190px,#f6f1e8 0,#ebe3d6 60%,transparent 100%),
    radial-gradient(ellipse 80px 110px at 260px 230px,#6e4630,transparent 100%),
    radial-gradient(ellipse 160px 80px at 200px 320px,#b07a4c,transparent 100%),
    linear-gradient(120deg,#2a221e 0%,#3e3028 45%,#2b2420 100%)}

/* collection */
.collection{left:0;top:2021px;width:1200px;height:408px;background:var(--dark-band)}
.collection-title{left:0;top:36px;width:1200px;text-align:center;font-family:'Dosis',sans-serif;font-weight:600;font-size:24px;color:#d7d7d7}
.taste-card{top:84px;width:288px;height:288px;overflow:hidden}
.taste-card .caption{position:absolute;left:0;bottom:0;width:100%;height:72px;background:rgba(255,255,255,.72);font-family:'Satisfy',cursive;font-size:32px;text-align:center;line-height:72px}
.taste-winter{left:149px;background:
    radial-gradient(circle at 25% 30%,#8ea66a 0 50px,transparent 56px),
    radial-gradient(circle at 75% 25%,#93ab70 0 50px,transparent 56px),
    radial-gradient(circle at 50% 62%,#86a062 0 56px,transparent 62px),
    linear-gradient(160deg,#4e6238,#5d7444)}
.taste-winter .caption{color:#7a8a3a}
.taste-autumn{left:456px;background:
    radial-gradient(ellipse 160px 110px at 50% 45%,#f6df84,transparent 100%),
    linear-gradient(160deg,#e3bf50,#d9b444)}
.taste-autumn .caption{color:#c99a1e}
.taste-summer{left:763px;background:
    radial-gradient(circle at 30% 30%,#f6f0ec 0 18px,transparent 20px),
    radial-gradient(circle at 68% 22%,#f6f0ec 0 18px,transparent 20px),
    radial-gradient(circle at 50% 55%,#f6f0ec 0 18px,transparent 20px),
    radial-gradient(circle at 22% 62%,#f6f0ec 0 16px,transparent 18px),
    radial-gradient(circle at 80% 58%,#f6f0ec 0 16px,transparent 18px),
    linear-gradient(160deg,#c8303b,#d8404c 50%,#b5262f)}
.taste-summer .caption{color:#c8303b}

/* story band */
.story-band{left:0;top:2429px;width:1200px;height:158px;background:var(--coral);color:var(--white);text-align:center}
.story-band h2{position:absolute;left:0;top:34px;width:100%;font-size:24px;font-weight:700}
.story-band p{position:absolute;left:0;top:86px;width:100%;font-size:11px;line-height:18px}

/* blog */
.blog-band{left:0;top:2700px;width:1200px;height:468px;background:var(--grey-band)}
.blog-card{top:2731px;width:288px;height:408px;background:var(--white)}
.blog-card .meta{position:absolute;left:14px;top:14px;font-size:10px;font-weight:700;color:var(--muted)}
.blog-card .meta span{color:#9a9a9a;font-weight:400}
.blog-card h3{position:absolute;left:14px;top:36px;font-size:14px;font-weight:700}
.blog-card .thumb{position:absolute;left:0;top:77px;width:288px;height:211px}
.blog-card .excerpt{position:absolute;left:14px;top:306px;width:260px;font-size:11px;line-height:15px;color:var(--muted)}
.blog-card .btn{position:absolute;left:82px;top:365px;width:124px;height:34px;background:var(--coral-btn);color:var(--white);font-size:10px;font-weight:900;text-align:center;line-height:34px}
.card-one{left:149px}
.card-two{left:456px}
.card-three{left:763px}
.thumb-photoloop{background:
    radial-gradient(ellipse 60px 50px at 25% 40%,#f1eadf,transparent 100%),
    radial-gradient(ellipse 60px 50px at 62% 70%,#f1eadf,transparent 100%),
    radial-gradient(ellipse 60px 50px at 85% 35%,#f1eadf,transparent 100%),
    linear-gradient(150deg,#8c78c8,#9d8ad4 50%,#6e5cae)}
.thumb-crunch{background:
    radial-gradient(ellipse 150px 110px at 50% 55%,#e2c29c,transparent 100%),
    linear-gradient(150deg,#9c7450,#c99b6f 50%,#7a5436)}
.thumb-giftbox{background:
    radial-gradient(ellipse 130px 90px at 50% 50%,#8a6a48,transparent 100%),
    linear-gradient(150deg,#e6dcc8,#d0bd96 50%,#b79a6c)}

/* newsletter */
.newsletter{left:0;top:3168px;width:1200px;height:250px;background:var(--sky);text-align:center}
.newsletter h2{position:absolute;left:0;top:38px;width:100%;font-size:30px;font-weight:400;color:var(--navy)}
.newsletter .rule{position:absolute;left:576px;top:84px;width:48px;height:3px;background:var(--navy)}
.newsletter p{position:absolute;left:0;top:96px;width:100%;font-size:14px;color:#333}
.signup{position:absolute;left:379px;top:144px;width:408px;height:43px;background:var(--white);border:2px solid #e4f4f7}
.signup .field{position:absolute;left:10px;top:12px;font-size:13px;color:#888}
.signup .submit{position:absolute;right:6px;top:7px;width:100px;height:27px;background:var(--teal);font-size:12px;font-weight:700;line-height:27px;color:#123}

/* footer */
.site-footer{left:0;top:3418px;width:1200px;height:182px;background:var(--white)}
.footer-col{top:45px;font-size:15px;line-height:22px;color:var(--navy)}
.col-shop{left:211px}
.col-policy{left:396px}
.col-social{left:631px;line-height:29px}
.col-social li{display:flex;align-items:center;gap:12px}
.col-social .sq{width:16px;height:16px;background:var(--navy)}
.col-social li:last-child .sq{background:var(--coral)}
.footer-col ul{list-style:none}
.payments{left:859px;top:62px;width:150px;display:grid;grid-template-columns:repeat(3,auto);gap:16px 14px;font-size:13px;font-weight:700;color:#555}
</style>
</head>
<body>

<div class="abs top-bar">
  <span class="abs promo">FREE SHIPPING AND RETURNS</span>
  <span class="abs contact">Contact &nbsp;|&nbsp; 0123-45-6789 &nbsp;|&nbsp; info@varubofoods.com</span>
</div>

<header class="abs site-header">
  <div class="abs brand"><span class="brand-dot"></span><span class="brand-name">varubo</span></div>
  <div class="abs account-links">LOG IN &nbsp; | &nbsp; REGISTER</div>
  <nav class="abs main-nav">
    <span>HOME</span><span>PRODUCTS</span><span>ABOUT US</span><span>CONTACT US</span>
    <svg width="14" height="14" viewBox="0 0 14 14" aria-label="Search"><circle cx="6" cy="6" r="4.2" fill="none" stroke="#7cc242" stroke-width="2"/><line x1="9" y1="9" x2="13" y2="13" stroke="#7cc242" stroke-width="2"/></svg>
    <svg width="16" height="14" viewBox="0 0 16 14" aria-label="Cart"><path d="M1 1h3l2 8h8l1.5-6H5" fill="none" stroke="#7cc242" stroke-width="2"/><circle cx="7" cy="12" r="1.4" fill="#7cc242"/><circle cx="13" cy="12" r="1.4" fill="#7cc242"/></svg>
  </nav>
</header>

<section class="abs hero" role="img" aria-label="Darkened photo of a family sharing healthy snacks at a kitchen table">
  <h1 class="abs hero-title">Welcome to Varubo Foods</h1>
  <p class="abs hero-tagline">Fuel for the Daily Trail-Seeker™</p>
</section>

<section class="abs intro">
  <p class="lead">We sell delicious, nutritious snacks and desserts that most closely comply with the paleo diet guidelines</p>
  <p>Our products are raw, organic, vegan, gluten-free, dairy-free, fiber-rich, nutrient-dense, antioxidant-rich<br>real foods with no preservatives, noadded sugar, and no artificial or plant-based sweeteners.<br>And they are irresistibly scrumptious!</p>
</section>

<h2 class="abs section-title" style="top:942px">Featured Products</h2>
<div class="abs section-rule" style="top:991px"></div>

<div class="abs media-grenamo" role="img" aria-label="Grenamo chocolate ball package with round label"></div>
<p class="abs product-label" style="left:288px;top:1466px;width:384px">Grenamo - $10</p>
<div class="abs media-cups" role="img" aria-label="Stack of mint baking cups"></div>
<p class="abs product-label" style="left:746px;top:1243px;width:238px">Plain Baking Cups - $4</p>
<div class="abs media-jimmies" role="img" aria-label="Bowl of pink jimmies"></div>
<p class="abs product-label" style="left:746px;top:1470px;width:238px">Jimmies - $3</p>
<div class="abs media-toppers" role="img" aria-label="Pink ice cream cone sugar toppers"></div>
<p class="abs product-label" style="left:214px;top:1694px;width:237px">Sugar Toppers - $9.50</p>
<div class="abs media-nonpareils" role="img" aria-label="Bowl of green non-pareils"></div>
<p class="abs product-label" style="left:214px;top:1922px;width:237px">Non-Pareils - $4</p>
<div class="abs media-mousse" role="img" aria-label="Glass of layered chocolate and cream mousse with strawberries"></div>
<p class="abs product-label" style="left:480px;top:1922px;width:504px">Mousse - $8.50</p>

<section class="abs collection">
  <h2 class="abs collection-title">Collection taste</h2>
  <div class="abs taste-card taste-winter" role="img" aria-label="Green glazed winter cookies"><span class="caption">Winter Taste</span></div>
  <div class="abs taste-card taste-autumn" role="img" aria-label="Yellow autumn sponge cake"><span class="caption">Autumn Taste</span></div>
  <div class="abs taste-card taste-summer" role="img" aria-label="Red velvet summer cookies with white chips"><span class="caption">Summer Taste</span></div>
</section>

<section class="abs story-band">
  <h2>One special cookie can change your world</h2>
  <p>Our products are inspired by the people and world around us. Beautiful, high-quality goods that are designed especially for you.<br>Discover our store and meet the people that make our brand what it is.</p>
</section>

<h2 class="abs section-title" style="top:2624px">Fresh From The Blog</h2>
<div class="abs section-rule" style="top:2674px"></div>

<div class="abs blog-band"></div>
<article class="abs blog-card card-one">
  <p class="meta">MARTA LINDQVIST <span>/ JANUARY 16, 2015</span></p>
  <h3>We love you on Photoloop</h3>
  <div class="thumb thumb-photoloop" role="img" aria-label="Decorated camera-shaped cookies on a purple backdrop"></div>
  <p class="excerpt">"If this gingerbread could talk, he'd wish you happy holidays" thanks for the special delivery.</p>
  <span class="btn">READ MORE</span>
</article>
<article class="abs blog-card card-two">
  <p class="meta">MARTA LINDQVIST <span>/ JANUARY 16, 2015</span></p>
  <h3>New Muscovado crunch</h3>
  <div class="thumb thumb-crunch" role="img" aria-label="Bowl of chocolate chip cookie dough"></div>
  <p class="excerpt">A new recipe for this bestseller - discover this new flavor now on our eshop</p>
  <span class="btn">READ MORE</span>
</article>
<article class="abs blog-card card-three">
  <p class="meta">MARTA LINDQVIST <span>/ JANUARY 09, 2015</span></p>
  <h3>Signature gift box</h3>
  <div class="thumb thumb-giftbox" role="img" aria-label="Gift box filled with assorted cookies"></div>
  <p class="excerpt">Signature gift box with an interior cloud print, made from 100% recycled cardboard.</p>
  <span class="btn">READ MORE</span>
</article>

<section class="abs newsletter">
  <h2>Subscribe To Our Newsletter</h2>
  <div class="rule"></div>
  <p>Sign up to stay in the loop. Receive updates, access to exclusive deals, and more.</p>
  <div class="signup"><span class="field">Your email</span><span class="submit">SUBSCRIBE</span></div>
</section>

<footer class="abs site-footer">
  <div class="abs footer-col col-shop"><ul><li>All Products</li><li>Blog</li><li>Faq</li><li>Contact Us</li></ul></div>
  <div class="abs footer-col col-policy"><ul><li>Privacy Policy</li><li>Shipping &amp; Return Policy</li><li>Terms of Service</li></ul></div>
  <div class="abs footer-col col-social"><ul><li><span class="sq"></span>Socialnest</li><li><span class="sq"></span>Chirpline</li><li><span class="sq"></span>Pinvale</li></ul></div>
  <div class="abs payments"><span>Paxa</span><span>Cardora</span><span>Orbix</span><span>Paywell</span><span>Novacard</span></div>
</footer>

</body>
</html>
```